Create a backdrop for a trade show booth!

We are looking for a design to put on a 10'X10' trade show booth for our company: Marlow Frost Jet.

Please see website: www.marlowfrostjet.com

Industry/Entity Type

It Company

```html
<!DOCTYPE html>
<html lang="en">
<head>
<meta charset="utf-8">
<title>Marlow Frost Jet — Wet-Ice Blasting</title>
<link href="https://fonts.googleapis.com/css2?family=Berkshire+Swash&family=Tinos:wght@700&display=swap" rel="stylesheet">
<style>
  :root {
    --sky-top: #3f93d6;
    --sky-mid: #7cbbe9;
    --sky-bottom: #e4f1fb;
    --ray: rgba(255, 255, 255, 0.10);
    --ink: #0d0d12;
    --navy: #14142a;
    --panel-blue: #00a2ea;
    --panel-frame: #0a0a0a;
    --frame-olive: #8a7a4a;
    --paper: #ffffff;
    --sand: #edc99b;
    --white: #ffffff;
    --serif: "Tinos", "Times New Roman", serif;
    --script: "Berkshire Swash", cursive;
  }
  * { margin: 0; padding: 0; box-sizing: border-box; }
  html, body { width: 1200px; height: 1200px; overflow: hidden; }
  body {
    position: relative;
    font-family: var(--serif);
    font-weight: 700;
    color: var(--ink);
    background:
      repeating-conic-gradient(from 200deg at 0% 0%, var(--ray) 0deg 6deg, transparent 6deg 13deg),
      linear-gradient(180deg, var(--sky-top) 0%, var(--sky-mid) 45%, var(--sky-bottom) 100%);
  }
  .headline { position: absolute; left: 300px; top: 40px; width: 620px; height: 130px; }
  .headline text {
    font-family: var(--script);
    font-size: 66px;
    fill: var(--navy);
    stroke: var(--white);
    stroke-width: 1.5px;
    paint-order: stroke;
  }
  .subtitle {
    position: absolute; left: 0; top: 134px; width: 1200px;
    text-align: center; padding-left: 0; font-size: 25px; color: var(--navy);
    transform: translateX(-15px);
  }
  .benefit {
    position: absolute; left: 35px; font-size: 29px; color: var(--white);
    text-shadow: -2px -2px 0 var(--ink), 2px -2px 0 var(--ink), -2px 2px 0 var(--ink), 2px 2px 0 var(--ink), 3px 3px 4px rgba(0,0,0,.5);
  }
  .benefit--one { top: 238px; }
  .benefit--two { top: 289px; }
  .section-title { position: absolute; font-size: 28px; color: var(--ink); }
  .info-panel {
    position: absolute;
    border: 9px solid var(--panel-frame);
    border-radius: 14px;
    background: var(--panel-blue);
    box-shadow: inset 0 0 0 3px #4a4a4a, 2px 3px 4px rgba(0,0,0,.35);
    display: flex; align-items: center; justify-content: center;
    text-align: center; font-size: 27px; line-height: 1.3; color: var(--ink);
  }
  .diagram {
    position: absolute;
    border: 9px solid var(--frame-olive);
    outline: 2px solid #c9bd93;
    background: linear-gradient(180deg, var(--paper) 0%, var(--paper) 62%, var(--sand) 72%, var(--sand) 100%);
  }
</style>
</head>
<body>
  <svg class="headline" viewBox="0 0 620 130" aria-label="wet-ice blasting">
    <defs>
      <path id="headline-arc" d="M 20 115 Q 310 10 600 115" fill="none"/>
    </defs>
    <text><textPath href="#headline-arc" startOffset="50%" text-anchor="middle">wet-ice blasting</textPath></text>
  </svg>
  <p class="subtitle">(frozen water blasting)</p>

  <p class="benefit benefit--one">1-environmentally-friendly and efficient cleaning process</p>
  <p class="benefit benefit--two">2-there is no damage to the surface being cleaned</p>

  <h2 class="section-title" style="left:37px; top:378px;">Resource Usage</h2>
  <div class="info-panel" style="left:11px; top:417px; width:653px; height:160px;">
    The Marlow Frost Jet uses an efficient 33<br>gallons (121 L) of water per hour of cleaning
  </div>

  <h2 class="section-title" style="left:38px; top:590px; font-size:26px;">Environmental Impact</h2>
  <div class="info-panel" style="left:11px; top:643px; width:653px; height:163px;">
    Abrasive blasting using sand, plastic beads, or<br>other media poses a danger for the environment
  </div>

  <h2 class="section-title" style="left:15px; top:828px;">Employee Safety</h2>
  <div class="info-panel" style="left:11px; top:882px; width:788px; height:160px;">
    In the industrial cleaning sector, airborne contaminants<br>are a prime concern when performing any cleaning task
  </div>

  <h2 class="section-title" style="left:15px; top:1062px; font-size:26px;">Cleaning Effectiveness</h2>
  <div class="info-panel" style="left:14px; top:1107px; width:882px; height:83px; font-size:24px;">
    The cleaning method used in wet-ice blasting falls under three steps:
  </div>

  <div class="diagram" style="left:778px; top:292px; width:389px; height:225px;" role="img" aria-label="Diagram: ice particle strikes a coating on the surface and flakes of grime fly off"></div>
  <div class="diagram" style="left:785px; top:563px; width:375px; height:229px;" role="img" aria-label="Diagram: ice particle flattens against the surface and slides beneath the grime"></div>
  <div class="diagram" style="left:824px; top:833px; width:340px; height:223px;" role="img" aria-label="Diagram: melted ice and water carry loosened dirt away from the clean surface"></div>
</body>
</html>
```